One page flyer for nonprofit focused IT company

I need a one page flyer (one side of a single 8.5x11 page) with text and graphics. The company logo is already done, and it must appear on the flyer along with other icons and graphics. The final design will be printed on heavy weight glossy paper as a handout and also distributed as a PDF.

The text is provided in an attachment, if it needs to be shortened let me know.

Industry/Entity Type

Information Technology

Requirements
Must have
• some flare (colors, icons or images)
Should not have
• While we work for nonprofits, my company is a FOR PROFIT company.

```html
<!DOCTYPE html>
<html lang="en">
<head>
<meta charset="utf-8">
<title>Corvane Systems Corporation – Nonprofit IT Services Flyer</title>
<link href="https://fonts.googleapis.com/css2?family=Poppins:wght@300;400;500;600&display=swap" rel="stylesheet">
<style>
  :root{
    --brand-red:#8b1a1f;
    --ink:#222226;
    --charcoal:#1f1f22;
    --grey:#9a9a9c;
    --white:#ffffff;
    --text-dark:#2b2b2b;
    --body-grey:#3a3a3a;
  }
  html,body{margin:0;padding:0;overflow:hidden;background:#fff;}
  .flyer{
    position:relative;width:928px;height:1200px;overflow:hidden;
    font-family:"Poppins",sans-serif;color:var(--text-dark);background:#fff;
  }
  .abs{position:absolute;}

  /* header */
  .hero-photo{left:0;top:152px;width:928px;height:348px;
    background:radial-gradient(ellipse at 62% 55%,#7d8694 0%,#4a505a 35%,#2b2e34 70%,#1e2024 100%);}
  .header-shapes{left:0;top:0;width:928px;height:200px;}
  .brand{left:60px;top:98px;display:flex;align-items:center;gap:10px;}
  .brand-mark{width:22px;height:22px;background:var(--brand-red);}
  .brand-name{font-weight:500;font-size:27px;color:var(--brand-red);letter-spacing:.3px;white-space:nowrap;}
  .header-title{left:505px;top:27px;width:400px;text-align:center;color:var(--white);
    font-weight:600;font-size:33px;line-height:41px;margin:0;white-space:nowrap;}

  .headline-box{left:0;top:428px;width:498px;height:72px;background:rgba(139,26,31,.88);}
  .headline{left:30px;top:437px;margin:0;color:var(--white);font-weight:600;font-size:22.5px;line-height:30px;}

  .intro{left:0;top:500px;width:928px;height:114px;background:var(--charcoal);}
  .intro p{margin:0;padding:14px 30px 0;color:var(--white);font-weight:300;font-size:15.4px;line-height:20px;letter-spacing:-.25px;}

  /* successes */
  .successes{left:0;top:614px;width:928px;height:226px;background:var(--brand-red);color:var(--white);}
  .section-title{margin:0;text-align:center;font-weight:600;font-size:26px;letter-spacing:.5px;}
  .successes .section-title{padding-top:12px;}
  .success{position:absolute;top:54px;}
  .success h3{margin:0 0 6px;font-size:14.5px;line-height:18px;font-weight:600;}
  .success p{margin:0;font-weight:300;font-size:11px;line-height:14.6px;letter-spacing:-.3px;}
  .success strong{font-weight:600;}
  .success-cost{left:30px;width:262px;}
  .success-membership{left:332px;width:262px;}
  .success-overhead{left:639px;width:270px;}

  /* solutions */
  .solutions{left:0;top:840px;width:928px;height:360px;
    background:linear-gradient(180deg,#e6e6e8 0%,#f7f7f8 12%,#ffffff 40%,#f3f3f4 100%);}
  .solutions .section-title{color:var(--ink);padding-top:22px;}
  .solution{position:absolute;}
  .solution-icon{position:absolute;width:50px;height:50px;}
  .solution-left .solution-icon{left:-67px;}
  .solution-right .solution-icon{left:-69px;}
  .solution h4{margin:0 0 5px;font-size:14.5px;line-height:18px;font-weight:500;color:var(--ink);}
  .solution p{margin:0;font-weight:300;font-size:11px;line-height:14.6px;letter-spacing:-.3px;color:var(--body-grey);}

  .footer-tab{left:311px;top:1157px;width:307px;height:43px;}
  .footer-url{left:311px;top:1166px;width:307px;text-align:center;color:var(--white);font-size:17px;}
</style>
</head>
<body>
<div class="flyer">

  <div class="abs hero-photo" role="img" aria-label="Photo of a hand touching a glowing cloud network diagram with device and document icons"></div>

  <svg class="abs header-shapes" viewBox="0 0 928 200" aria-hidden="true">
    <polygon points="0,0 470,0 370,193 0,193" fill="#ffffff"/>
    <polygon points="470,0 482,0 383,170 372,170" fill="#a3a3a5"/>
    <polygon points="477,0 928,0 928,152 413,152" fill="#8b1a1f"/>
    <rect x="66" y="186" width="178" height="15" fill="#9a9a9c"/>
  </svg>

  <div class="abs brand">
    <span class="brand-mark"></span>
    <span class="brand-name">Corvane Systems</span>
  </div>

  <h1 class="abs header-title">50 Years of<br>NonProfit IT Services</h1>

  <div class="abs headline-box"></div>
  <h2 class="abs headline">An Efficient and Elegant Approach to<br>IT Solution Implementations</h2>

  <div class="abs intro">
    <p>Corvane Systems Corporation has been supporting the Information Systems needs of nonprofits for over 50 years. We continually strive to bring the latest technologies and best practices to nonprofits to drive down the cost of IT while implementing systems that drive revenue. Our Agile approach to IT management means that we deliver working systems to every one of our clients every two weeks.</p>
  </div>

  <section class="abs successes">
    <h2 class="section-title">SUCCESSES</h2>
    <div class="success success-cost">
      <h3>90% Reduction in Software<br>Development Costs</h3>
      <p>Keystone Research's National Vehicle Retailers Association needed to update their core product offering; they engaged their in-house IT department who estimated the project would take 3 years at a cost of $3,000,000. NVRA decided to work with Corvane Systems Corporation instead, and the product was released to production in only 9 months at <strong>one tenth of the cost</strong>, only $300,000</p>
    </div>
    <div class="success success-membership">
      <h3>10x Increase in Membership</h3>
      <p>Greenway Paths Alliance needed to move to online membership registration and contracted with Corvane Systems Corporation to build a significant online presence and engage potential members. Through compelling online tools and mobile applications Greenway Paths has <strong>increased membership 10 fold.</strong></p>
    </div>
    <div class="success success-overhead">
      <h3>20% Reduction in Overhead</h3>
      <p>The National Alliance of Civic Leaders had antiquated systems and processes in place to manage over 500 chapters across the nation. Working with CSC they implemented online tools to allow communication and management between the local chapters and national headquarters. This eliminated much of the overhead of chapter management, <strong>reducing HR costs by 20%.</strong></p>
    </div>
  </section>

  <section class="abs solutions">
    <h2 class="section-title">SOLUTIONS</h2>

    <div class="solution solution-left" style="left:110px;top:77px;width:345px;">
      <svg class="solution-icon" style="top:-5px;" viewBox="0 0 50 50" aria-hidden="true"><circle cx="25" cy="25" r="23" fill="#fff" stroke="#8b1a1f" stroke-width="2.2"/><rect x="13" y="15" width="24" height="19" rx="2" fill="none" stroke="#8b1a1f" stroke-width="2"/><line x1="13" y1="20" x2="37" y2="20" stroke="#8b1a1f" stroke-width="2"/></svg>
      <h4>Web Applications</h4>
      <p>With a focus on non-profit websites and web based applications, CSC helps nonprofits communicate with their members and donors while maximizing online giving and engagement.</p>
    </div>

    <div class="solution solution-left" style="left:110px;top:161px;width:345px;">
      <svg class="solution-icon" style="top:-3px;" viewBox="0 0 50 50" aria-hidden="true"><circle cx="25" cy="25" r="23" fill="#fff" stroke="#8b1a1f" stroke-width="2.2"/><rect x="17" y="12" width="15" height="26" rx="2" fill="none" stroke="#8b1a1f" stroke-width="2"/><circle cx="29" cy="25" r="4" fill="#8b1a1f"/><line x1="22" y1="34" x2="27" y2="34" stroke="#8b1a1f" stroke-width="2"/></svg>
      <h4>Mobile Applications</h4>
      <p>Corvane Systems Corporation implements mobile applications for all major phone platforms to provide direct communications with members and donors enabling real-time, two way interaction.</p>
    </div>

    <div class="solution solution-left" style="left:110px;top:244px;width:345px;">
      <svg class="solution-icon" style="top:-1px;" viewBox="0 0 50 50" aria-hidden="true"><circle cx="25" cy="25" r="23" fill="#fff" stroke="#8b1a1f" stroke-width="2.2"/><rect x="12" y="14" width="7" height="9" fill="none" stroke="#8b1a1f" stroke-width="1.8"/><rect x="21.5" y="14" width="7" height="9" fill="none" stroke="#8b1a1f" stroke-width="1.8"/><rect x="31" y="14" width="7" height="9" fill="none" stroke="#8b1a1f" stroke-width="1.8"/><path d="M15.5 23v5h19v-5M25 23v10" fill="none" stroke="#8b1a1f" stroke-width="1.8"/><rect x="19" y="33" width="12" height="5" fill="#8b1a1f"/></svg>
      <h4>Systems Integration</h4>
      <p>Every nonprofit's IT applications are scattered and disconnected. Corvane Systems Corporation has decades of experience integrating these applications into a single cohesive system.</p>
    </div>

    <div class="solution solution-right" style="left:555px;top:77px;width:355px;">
      <svg class="solution-icon" style="top:-9px;" viewBox="0 0 50 50" aria-hidden="true"><circle cx="25" cy="25" r="23" fill="#fff" stroke="#8b1a1f" stroke-width="2.2"/><rect x="14" y="13" width="18" height="22" rx="2" fill="none" stroke="#8b1a1f" stroke-width="2"/><circle cx="23" cy="21" r="3" fill="none" stroke="#8b1a1f" stroke-width="1.8"/><path d="M18 30c1-4 9-4 10 0" fill="none" stroke="#8b1a1f" stroke-width="1.8"/><circle cx="34" cy="33" r="4" fill="#8b1a1f"/></svg>
      <h4>Business Intelligence and Reporting</h4>
      <p>Corvane Systems Corporation can wrestle all of an organization's data into simple executive dashboards and reports.</p>
    </div>

    <div class="solution solution-right" style="left:555px;top:146px;width:355px;">
      <svg class="solution-icon" style="top:-3px;" viewBox="0 0 50 50" aria-hidden="true"><circle cx="25" cy="25" r="23" fill="#fff" stroke="#8b1a1f" stroke-width="2.2"/><path d="M16 30a6 6 0 0 1 1-12 8 8 0 0 1 15 1 5.5 5.5 0 0 1 1 11z" fill="none" stroke="#8b1a1f" stroke-width="2"/><path d="M25 36v-11M21 28l4-4 4 4" fill="none" stroke="#8b1a1f" stroke-width="2"/></svg>
      <h4>Cloud Migration</h4>
      <p>Reduce IT costs by migrating to the latest cloud solutions.</p>
    </div>

    <div class="solution solution-right" style="left:555px;top:204px;width:355px;">
      <svg class="solution-icon" style="top:14px;" viewBox="0 0 50 50" aria-hidden="true"><circle cx="25" cy="25" r="23" fill="#fff" stroke="#8b1a1f" stroke-width="2.2"/><rect x="15" y="12" width="20" height="25" rx="2" fill="none" stroke="#8b1a1f" stroke-width="2"/><line x1="19" y1="20" x2="31" y2="20" stroke="#8b1a1f" stroke-width="1.8"/><line x1="19" y1="25" x2="31" y2="25" stroke="#8b1a1f" stroke-width="1.8"/><path d="M19 31l3 3 6-6" fill="none" stroke="#8b1a1f" stroke-width="2"/></svg>
      <h4>Member Donor Database</h4>
      <p>Corvane Systems Corporation's PledgeLoom Member / Donor CRM system is fully customized for each client meeting the unique needs of your organization.</p>
    </div>
  </section>

  <svg class="abs footer-tab" viewBox="0 0 307 43" aria-hidden="true"><path d="M12 10 Q16 0 28 0 H276 Q288 0 292 10 L307 43 H0 Z" fill="#8b1a1f"/></svg>
  <div class="abs footer-url">www.corvanesystems.com</div>

</div>
</body>
</html>
```